Poster Design Job - Winner can do follow-up business

- Kalvuro.com is a Swiss-based online store selling business shirts and accessories for business men
- Please visit the webpage to make yourself familiar with the company. Although the text is in German, with Google translator you should be able to understand the main content.
- Our clients are mainly business men between 30 and 60 years old. Mostly with a high income working in the service industry (banking, insurance, lawyers, etc.). Sometimes there wives purchase the shirts for them ;-)
- The colors and the logo are given, as they are also used for the print materials (please see files in attachment)
- I am running several businesses and often need a talented web designer --> the winner gets substantial follow-up business
your task:
- For our company we need a poster for a larger billboard advertisement campaign. We plan to book billboard space all over Switzerland.
- Please include in the poster the logo & the claim "Das Perfekte Hemd für jeden" "Passend | Einfach | Garantierte Qualität" in english this means "The perfect shirt for everybody" "Fitting | Simple | Guaranteed Quality"
- Also you need to include the following text - don`t change it:
Frühlingsaktion 20 Franken Gutschein für Ihr erstes Kalvuro-Hemd auf www.kalvuro.com. Gutscheincode: Frühling
-The text means: Spring Sale 20 CHF off for your first Kalvuro shirt on www.kalvuro.com. Your coupon code: Spring
-Don`t change the Logo or our corporate colors
-All images that are on the website are available. Please just ask jb@kalvuro.com!
- Format should be A0 - 841 x 1189mm - Portrait
Reason: Need some more time to work on the designs handed in by the designers.
Best,
Dorian

```html
<!DOCTYPE html>
<html lang="de">
<head>
<meta charset="utf-8">
<title>Kalvuro Poster</title>
<link rel="stylesheet" href="https://fonts.googleapis.com/css2?family=Josefin+Sans:wght@400;600;700&family=Open+Sans:wght@400;600&display=swap">
<style>
  :root {
    --red: #a8211f;
    --red-dark: #8e1816;
    --red-light: #b52622;
    --navy: #15152a;
    --navy-mid: #0e0e20;
    --navy-deep: #070716;
    --badge: #05050f;
    --gold: #e9d35f;
    --white: #ffffff;
    --muted: #b9b9cc;
    --shirt: #cdc3da;
    --shirt-shade: #a596bb;
    --trouser: #2e3140;
  }
  html, body { margin: 0; padding: 0; overflow: hidden; }
  body { width: 1200px; height: 862px; background: var(--navy-deep); }
  .poster { position: relative; width: 1200px; height: 862px; overflow: hidden; }
  .backdrop { position: absolute; inset: 0; }

  .model-photo {
    position: absolute; left: 232px; top: 0; width: 387px; height: 862px;
    background:
      linear-gradient(90deg, rgba(0,0,0,0.18) 0%, rgba(0,0,0,0) 30%, rgba(0,0,0,0) 100%),
      linear-gradient(180deg, var(--shirt) 0%, var(--shirt-shade) 76%, #3b3d4c 80%, var(--trouser) 100%);
  }

  .badge {
    position: absolute; left: 38px; top: 164px; width: 316px; height: 316px;
    border-radius: 50%; background: var(--badge);
    display: flex; flex-direction: column; align-items: center; justify-content: center;
  }
  .brand-name {
    font-family: "Josefin Sans", sans-serif; font-weight: 600;
    font-size: 50px; letter-spacing: 2px; color: var(--gold);
    margin-top: 52px; line-height: 1;
  }
  .brand-url {
    font-family: "Open Sans", sans-serif; font-weight: 600;
    font-size: 21px; color: var(--white); margin-top: 28px; letter-spacing: 0.5px;
  }

  .frame-mark {
    position: absolute; left: 990px; top: 72px; width: 124px; height: 126px;
    border: 4px solid var(--white);
  }

  .message {
    position: absolute; left: 668px; top: 270px; width: 480px;
    font-family: "Josefin Sans", sans-serif; color: var(--white);
  }
  .claim {
    margin: 0; font-weight: 700; font-size: 44px; line-height: 1.12;
    color: var(--gold); letter-spacing: 0.5px;
  }
  .claim-values {
    margin: 18px 0 0; font-weight: 400; font-size: 22px; letter-spacing: 1px;
    color: var(--white);
  }
  .rule {
    width: 64px; height: 3px; background: var(--gold); margin: 34px 0 30px;
  }
  .offer-title {
    margin: 0; font-weight: 600; font-size: 30px; text-transform: uppercase;
    letter-spacing: 2px; color: var(--white);
  }
  .offer-text {
    margin: 12px 0 0; font-family: "Open Sans", sans-serif; font-weight: 400;
    font-size: 19px; line-height: 1.5; color: var(--muted);
  }
  .offer-text strong { color: var(--white); font-weight: 600; }
  .coupon {
    display: inline-block; margin-top: 24px; padding: 12px 22px 9px;
    border: 2px solid var(--gold);
    font-weight: 600; font-size: 22px; letter-spacing: 1px; color: var(--white);
  }
  .coupon span { color: var(--gold); }
</style>
</head>
<body>
<main class="poster">
  <svg class="backdrop" width="1200" height="862" viewBox="0 0 1200 862" aria-hidden="true">
    <rect x="0" y="0" width="620" height="862" fill="var(--red)"/>
    <polygon points="0,500 620,360 620,862 0,862" fill="var(--red-light)"/>
    <polygon points="0,650 620,520 620,862 0,862" fill="var(--red-dark)"/>
    <rect x="619" y="0" width="581" height="862" fill="var(--navy)"/>
    <polygon points="619,360 1200,200 1200,862 619,862" fill="var(--navy-mid)"/>
    <polygon points="619,480 1200,260 1200,862 619,862" fill="var(--navy-deep)"/>
    <polygon points="900,862 1200,740 1200,862" fill="#05050f"/>
  </svg>

  <div class="model-photo" role="img" aria-label="Photo of a man in a striped business shirt, tie and dark trousers"></div>

  <div class="badge">
    <div class="brand-name">KALVURO</div>
    <div class="brand-url">www.kalvuro.com</div>
  </div>

  <div class="frame-mark"></div>

  <section class="message">
    <h1 class="claim">Das Perfekte Hemd für jeden</h1>
    <p class="claim-values">Passend | Einfach | Garantierte Qualität</p>
    <div class="rule"></div>
    <h2 class="offer-title">Frühlingsaktion</h2>
    <p class="offer-text"><strong>20 Franken Gutschein</strong> für Ihr erstes Kalvuro-Hemd auf www.kalvuro.com.</p>
    <div class="coupon">Gutscheincode: <span>Frühling</span></div>
  </section>
</main>
</body>
</html>
```